Business Card

THIS IS THE CARD INFORMATION
DEVELOPMENT I FINANCING I PROPERTY MANAGEMENT
DANIEL FERRÁN
3186 NE 74th Terrace
Pine Harbor, FL 33418
Telephone I 855.274.6180
Facsimile I 855.274.6127
Industry/Entity Type
Business

```html
<!DOCTYPE html>
<html lang="en">
<head>
<meta charset="UTF-8">
<title>Navarro Ibáñez &amp; Company — Business Card</title>
<link rel="stylesheet" href="https://fonts.googleapis.com/css2?family=Open+Sans:wght@400;600;700&display=swap">
<style>
  :root {
    --backdrop: #e8e8e8;
    --card: #ffffff;
    --purple: #a3238f;
    --purple-deep: #72246b;
    --ink: #2a2a2a;
    --grey-text: #6e6e6e;
    --white: #ffffff;
  }
  * { box-sizing: border-box; margin: 0; padding: 0; }
  html, body {
    width: 1200px;
    height: 950px;
    overflow: hidden;
    background: var(--backdrop);
    font-family: "Open Sans", Arial, sans-serif;
  }
  .business-card {
    position: absolute;
    left: 230px;
    top: 262px;
    width: 740px;
    height: 424px;
    background: var(--card);
    overflow: hidden;
  }
  .arc-panel {
    position: absolute;
    left: 0;
    top: 0;
    width: 740px;
    height: 424px;
  }
  .brand {
    position: absolute;
    right: 60px;
    top: 56px;
    display: flex;
    align-items: center;
    gap: 14px;
    color: var(--ink);
    font-weight: 700;
  }
  .brand-dot {
    width: 66px;
    height: 66px;
    border-radius: 50%;
    background: var(--purple);
    flex: none;
  }
  .brand-name {
    display: flex;
    flex-direction: column;
    align-items: flex-end;
    line-height: 1;
  }
  .brand-name .primary {
    font-size: 37px;
    letter-spacing: 0.5px;
  }
  .brand-name .secondary {
    font-size: 17px;
    margin-top: 4px;
    letter-spacing: 0.5px;
  }
  .contact {
    position: absolute;
    left: 53px;
    top: 224px;
    color: var(--white);
  }
  .contact-name {
    font-size: 20px;
    font-weight: 700;
    letter-spacing: 0.3px;
    margin-bottom: 20px;
  }
  .contact-lines {
    font-size: 16px;
    line-height: 24px;
    font-weight: 400;
  }
  .contact-lines .label {
    font-weight: 700;
  }
  .services {
    position: absolute;
    right: 59px;
    top: 324px;
    text-align: right;
    color: var(--grey-text);
    font-size: 16px;
    font-weight: 600;
    letter-spacing: 1.6px;
    line-height: 23px;
  }
</style>
</head>
<body>
  <main class="business-card">
    <svg class="arc-panel" viewBox="0 0 740 424" aria-hidden="true">
      <defs>
        <linearGradient id="arcGradient" x1="1" y1="0" x2="0" y2="1">
          <stop offset="0" stop-color="#a3238f"/>
          <stop offset="1" stop-color="#72246b"/>
        </linearGradient>
      </defs>
      <circle cx="-3" cy="541" r="424" fill="url(#arcGradient)"/>
    </svg>

    <div class="brand">
      <span class="brand-dot"></span>
      <div class="brand-name">
        <span class="primary">NAVARRO IBÁÑEZ</span>
        <span class="secondary">&amp; COMPANY</span>
      </div>
    </div>

    <section class="contact">
      <p class="contact-name">DANIEL FERRÁN</p>
      <div class="contact-lines">
        <p>3186 NE 74th Terrace</p>
        <p>Pine Harbor, FL 33418</p>
        <p><span class="label">Telephone</span> 855.274.6180</p>
        <p><span class="label">Facsimile</span>&nbsp;&nbsp; 855.274.6127</p>
      </div>
    </section>

    <section class="services">
      <p>DEVELOPMENT | FINANCING</p>
      <p>PROPERTY MANAGEMENT</p>
    </section>
  </main>
</body>
</html>
```